Electrical contracting business specialising in smoke detector installation needs flyer design

i need a flyer design made up highlighting the fact that the Qld legislation is changing on smoke detectors in homes for everyones safety. I am an electrical contractor ( Tallow Bend Electrical) specialising in smoke detector installation to comply with the new Qld legislation. Some of the wording that can be used-
When you sleep, your sense of smell also sleeps. If a fire starts, toxic fumes canovercome you. Photoelectric smoke alarms see smoke and will alert you early, so you can escape. With interconnected alarms, you will be alerted no matter where you are, or where the fire starts.
New legislation specifies the type, positioning and interconnectedness of alarms, which are critical factors for an early warning and a quick escape.
To give your family the best chance of surviving a house fire, update your smoke alarms to match the new legislation as soon as you can. Call TBE on 0471385269

Target Market(s)

Body Corporates , people selling and renting their properties

Industry/Entity Type

Electrician

Colors

Designer to choose colors to be used in the design.

Requirements
Must have
• Safety aspect.

```html
<!DOCTYPE html>
<html lang="en">
<head>
<meta charset="utf-8">
<title>Tallow Bend Electrical – Smoke Alarm Flyer</title>
<link href="https://fonts.googleapis.com/css2?family=Quicksand:wght@300;500;700&family=Oswald:wght@300;500&family=Open+Sans:wght@400;600&display=swap" rel="stylesheet">
<style>
  :root{
    --stage:#e6e6ea;
    --night:#150c33;
    --violet:#2a1352;
    --deep:#0b0718;
    --gold:#e3a02e;
    --banner:#d99a3a;
    --white:#ffffff;
    --soft:#d8d2ea;
    --footer:#3f3d42;
  }
  *{box-sizing:border-box;margin:0;padding:0}
  html,body{width:1200px;height:1200px;overflow:hidden;background:var(--stage)}
  body{position:relative;font-family:"Open Sans",Arial,sans-serif;color:var(--white)}
  .page{position:absolute;top:206px;width:530px;height:750px;overflow:hidden;
    background:linear-gradient(180deg,var(--night) 0%,#1d0f40 55%,var(--violet) 100%)}
  .page--front{left:61px}
  .page--back{left:610px}
  .abs{position:absolute}
  .page-footer{position:absolute;left:0;bottom:0;width:100%;height:27px;background:var(--footer)}

  /* front */
  .intro{left:46px;top:42px;font-family:"Quicksand",sans-serif}
  .intro__lead{font-size:21px;font-weight:500;line-height:1.2}
  .intro__title{font-size:33px;font-weight:700;line-height:1.1}
  .scene-art{left:0;top:118px;width:530px;height:155px;
    background:radial-gradient(ellipse at 50% 60%,#7fb8e8 0%,#3b5f9a 40%,#1a1f4a 80%)}
  .sleep-band{left:0;top:273px;width:530px;height:145px;background:linear-gradient(90deg,#1245a8 0%,#1a5fc4 55%,#5b8fd8 100%)}
  .sleep-photo{left:270px;top:273px;width:260px;height:145px;
    background:radial-gradient(ellipse at 55% 50%,#cfe0f4 0%,#7fa6dc 45%,rgba(26,95,196,0) 85%)}
  .sleep-title{left:46px;top:286px;font-family:"Oswald",sans-serif;font-weight:500;font-size:20px;line-height:25px;text-transform:uppercase}
  .sleep-copy{left:46px;top:344px;width:222px;font-size:9.6px;line-height:12.8px}
  .legal-lead{left:46px;top:438px;width:275px;font-family:"Quicksand",sans-serif;font-weight:700;font-size:15.5px;line-height:19.5px;color:var(--gold)}
  .family-copy{left:46px;top:545px;width:200px;font-size:11.5px;line-height:15.2px}
  .detector-art{left:350px;top:420px;width:88px;height:80px;border-radius:50%;
    background:radial-gradient(circle at 50% 45%,#f2eefc 0%,#b7a8e6 40%,rgba(90,70,160,0) 75%)}
  .specialist{left:306px;top:522px;width:178px;text-align:center;font-family:"Quicksand",sans-serif;font-weight:300;font-size:12.2px;line-height:15px;letter-spacing:.2px}
  .specialist strong{font-weight:700;color:var(--gold)}
  .specialist em{display:block;font-style:normal;font-family:"Oswald",sans-serif;font-weight:300;font-size:11px;margin-top:3px}
  .badges{display:flex;gap:20px}
  .badge{width:40px;height:44px;background:#8a8399;border-radius:50%}
  .badge--crest{border-radius:6px;background:#c9c4d4}
  .front-badges,.back-badges{left:347px;top:618px}
  .licence-note{width:150px;text-align:center;font-size:4.6px;line-height:6px;color:var(--soft)}
  .front-note,.back-note{left:381px;top:673px;transform:translateX(-50%)}
  .call{left:46px;top:622px;font-family:"Quicksand",sans-serif;font-size:26px;font-weight:300;line-height:1}
  .call b{font-weight:700;color:var(--gold);font-size:32px}
  .biz-name{left:50px;top:670px;font-family:"Quicksand",sans-serif;font-weight:700;font-size:16px}
  .biz-phone{left:46px;top:690px;font-family:"Quicksand",sans-serif;font-weight:700;font-size:22px;color:var(--gold);letter-spacing:.3px}

  /* back */
  .banner{left:0;top:23px;width:420px;height:50px;background:var(--banner);font-family:"Quicksand",sans-serif;font-weight:700;text-align:right;padding:6px 30px 0 0}
  .banner__title{font-size:20.5px;line-height:22px}
  .banner__sub{font-size:14px;line-height:17px}
  .band{left:0;width:530px}
  .band--black{top:278px;height:188px;background:var(--deep)}
  .section-title{left:0;width:530px;text-align:center;font-weight:600;font-size:9.6px;text-decoration:underline;text-transform:uppercase}
  .col-left{left:46px;width:150px;font-size:7.2px;line-height:9.6px}
  .col-right{left:218px;width:280px;font-size:6.4px;line-height:8.6px}
  .date{font-family:"Quicksand",sans-serif;font-weight:700;font-size:10px;line-height:12px;color:var(--gold);text-decoration:underline}
  .subhead{font-family:"Quicksand",sans-serif;font-weight:700;font-size:10px;line-height:12px;text-decoration:underline;margin-top:11px}
  .col-right p{margin-bottom:5px}
  .back-mark{left:46px;top:648px;font-family:"Quicksand",sans-serif;font-weight:700;font-size:46px;color:var(--gold);line-height:1}
  .back-name{left:158px;top:677px;font-family:"Quicksand",sans-serif;font-weight:700;font-size:11px;line-height:13px}
  .back-name span{display:block;color:var(--gold)}
</style>
</head>
<body>

<section class="page page--front">
  <div class="abs intro">
    <p class="intro__lead">Are you up to speed with</p>
    <h1 class="intro__title">SMOKE ALARMS?</h1>
  </div>
  <div class="abs scene-art" role="img" aria-label="Illustration of a home at night with ceiling smoke alarms casting blue detection cones and a person escaping"></div>

  <div class="abs sleep-band"></div>
  <div class="abs sleep-photo" role="img" aria-label="Photo of a person sleeping in bed under blue night light"></div>
  <h2 class="abs sleep-title">When you sleep, your sense<br>of smell also sleeps</h2>
  <p class="abs sleep-copy">If a fire starts, toxic fumes canovercome you. Photoelectric smoke alarms see smoke and will alert you early, so you can escape. With interconnected alarms, you will be alerted no matter where you are, or where the fire starts.</p>

  <p class="abs legal-lead">New legislation specifies the type, positioning and interconnectedness of alarms, which are critical factors for an early warning and a quick escape.</p>
  <p class="abs family-copy">To give your family the best chance of surviving a house fire, update your smoke alarms to match the new legislation as soon as you can.</p>

  <div class="abs detector-art" role="img" aria-label="Photo of a ceiling smoke detector glowing in smoke"></div>
  <p class="abs specialist">SPECIALISED IN SMOKE<br>DETECTOR INSTALLATION<br>TO COMPLY WITH THE<br><strong>NEW QLD LEGISLATION</strong><em>(See complete details overleaf)</em></p>

  <div class="abs badges front-badges"><span class="badge"></span><span class="badge badge--crest"></span></div>
  <p class="abs licence-note front-note">© Regional Fire Safety Office 2016. Material in this document is licensed for reuse under a Creative Commons Attribution licence, except protected marks.</p>

  <p class="abs call">Call <b>TBE</b></p>
  <p class="abs biz-name">Tallow Bend Electrical</p>
  <p class="abs biz-phone">0471385269</p>
  <div class="page-footer"></div>
</section>

<section class="page page--back">
  <div class="abs banner">
    <h2 class="banner__title">NEW SMOKE ALARM LEGISLATION</h2>
    <p class="banner__sub">INFORMATION SHEET</p>
  </div>

  <h3 class="abs section-title" style="top:89px">For existing dwellings</h3>
  <div class="abs col-left" style="top:102px">
    <p class="date">From 1 January 2017</p>
    <p>When replacing smoke alarms, they must be of a photoelectric type which complies with Australian Standard (AS) 3786-2014.</p>
    <p class="subhead">Replacing smoke alarms</p>
    <p>Existing smoke alarms manufactured more than ten years ago must be replaced. (Note: Smoke alarms should have the date of manufacture stamped on them.) Smoke alarms that do not operate when tested must be replaced immediately. Existing hardwired smoke alarms that need replacement must be replaced with a hardwired smoke alarm.</p>
  </div>
  <div class="abs col-right" style="top:102px">
    <p class="date">From 1 January 2027</p>
    <p>Smoke alarms in all dwellings must:<br>i) be photoelectric (AS 3786-2014); and<br>ii) not also contain an ionisation sensor; and<br>iii) be less than 10 years old; and<br>iv) operate when tested; and<br>v) be interconnected with every other smoke alarm in the dwelling so all activate together.</p>
    <p>Smoke alarms must be installed on each storey:</p>
    <p>i) in each bedroom; and<br>ii) in hallways which connect bedrooms and the rest of the dwelling; or<br>iii) if there is no hallway, between the bedrooms and other parts of the storey; and<br>iv) if there are no bedrooms on a storey at least one smoke alarm must be installed in the most likely path of travel to exit the dwelling.</p>
    <p>Smoke alarms must be either hardwired or powered by a nonremovable 10-year battery.</p>
  </div>

  <div class="abs band band--black"></div>
  <h3 class="abs section-title" style="top:295px">Dwellings being sold, leased or an existing lease is renewed</h3>
  <div class="abs col-left" style="top:308px">
    <p class="date">From 1 January 2017</p>
    <p>Requirements as for<br>existing dwellings.<br>Existing landlord's and<br>tenant's obligations<br>regarding the installation<br>and testing of smoke<br>alarms continue.<br>Property sellers must<br>continue to lodge a Form<br>24 with the State<br>Titles Office<br>stating the requirements<br>of the smoke alarm<br>legislation have been met.</p>
  </div>
  <div class="abs col-right" style="top:308px">
    <p class="date">From 1 January 2022</p>
    <p>Smoke alarms in the dwelling must:<br>i) be photoelectric (AS 3786-2014); and<br>ii) not also contain an ionisation sensor; and<br>iii) be less than 10 years old; and<br>iv) operate when tested; and<br>v) be interconnected with every other smoke alarm in the dwelling so all activate together.</p>
    <p>Smoke alarms must be installed on each storey:<br>i) in each bedroom; and<br>ii) in hallways which connect bedrooms and the rest of the dwelling; or<br>iii) if there is no hallway, between the bedrooms and other parts of the storey; and<br>iv) if there are no bedrooms on a storey at least one smoke alarm must be installed in the most likely path of travel to exit the dwelling.</p>
    <p>Smoke alarms must be hardwired or powered by a non-removable 10-year battery.</p>
  </div>

  <h3 class="abs section-title" style="top:482px">New dwellings and dwellings being substantially renovated</h3>
  <div class="abs col-left" style="top:495px">
    <p class="date">From 1 January 2017</p>
    <p>The development<br>approval process for new<br>dwellings and substantial<br>renovations will ensure<br>that building approvals<br>received on or after this<br>date will bring dwellings<br>into compliance with the<br>new laws.</p>
  </div>
  <div class="abs col-right" style="top:508px">
    <p>Smoke alarms in the dwelling must:<br>i) be photoelectric (AS 3786-2014); and<br>ii) not also contain an ionisation sensor; and<br>iii) be hardwired to the mains power supply with a secondary power source (i.e. battery); and<br>iv) be interconnected with every other smoke alarm in the dwelling so all activate together.</p>
    <p>Smoke alarms must be installed on each storey:</p>
    <p>i) in each bedroom; and<br>ii) in hallways which connect bedrooms and the rest of the dwelling; or<br>iii) if there is no hallway, between the bedrooms and other parts of the storey; and<br>iv) if there are no bedrooms on a storey at least one smoke alarm must be installed in the most likely path of travel to exit the dwelling.</p>
  </div>

  <p class="abs back-mark">TBE</p>
  <p class="abs back-name">Tallow Bend Electrical<span>0471385269</span></p>
  <div class="abs badges back-badges"><span class="badge"></span><span class="badge badge--crest"></span></div>
  <p class="abs licence-note back-note">© Regional Fire Safety Office 2016. Material in this document is licensed for reuse under a Creative Commons Attribution licence, except protected marks.</p>
  <div class="page-footer"></div>
</section>

</body>
</html>
```